Review Site Redesign

We have a rather ambitious goal to reinvent (redesign) the way bank financial review sites present information. In that respect, we’re looking for an innovative creative design.
As examples of what I would call bad or boring design please look at the following sites:
1. http://brindlelend.example/se
2. http://corvalmoney.example/se/privatlan
3. http://fjellpurse.example/no
These are the traditional way these types of review sites are organized: dull and boring. I think we can do a lot better than that.
I need a site that will capture attention end engage the visitor; a site that will create a more interactive and less passive user experience.
Scope of work should also include logo font and additional content space for articles, FAQ, widgets, social media links, etc.

Not sure what to advise you as best format - maybe a flash or js carousel, gallery, wheel, logo image matrix, or something else.
Maybe some kind of interactive logo matrix such as this site: http://www.lumvikra.example/
Please apply your best creative mind work to this problem.
Also, please think about creative use of background images, stock photos, etc.
For logo font use can use URL “quillfunds.example” as placeholder.

Industry/Entity Type

Bank

```html
<!DOCTYPE html>
<html lang="en">
<head>
<meta charset="utf-8">
<title>VESTRANO – Bank Reviews</title>
<link rel="stylesheet" href="https://fonts.googleapis.com/css2?family=Arimo:ital,wght@0,400;0,700;1,400&family=Tinos&display=swap">
<style>
:root{
  --navy:#1d4f86;
  --blue:#2466ad;
  --link:#2a6bb0;
  --ink:#333;
  --btn:#5a5a5a;
  --card:#f3f3f3;
  --rule:#c9c9c9;
  --mark:#c9d3dd;
}
*{box-sizing:border-box;margin:0;padding:0}
html,body{width:811px;height:1200px;overflow:hidden}
body{position:relative;background:#fff;font-family:"Arimo",Arial,sans-serif;color:var(--ink)}
.abs{position:absolute}
.header-bg{left:0;top:0;width:811px;height:290px;background:linear-gradient(#cfeefa,#e9f7fc 70%,#fff)}
.brand{left:61px;top:14px;font-family:"Tinos","Times New Roman",serif;font-size:31px;color:var(--navy);letter-spacing:1px}
.search{left:621px;top:23px;width:128px;height:19px;background:#fff;border:1px solid #c8d3d8;font-size:8px;font-style:italic;color:#aaa;padding:4px 0 0 12px}
.search svg{position:absolute;right:8px;top:5px}
.hero{left:61px;top:69px;width:690px;height:149px;border:3px solid var(--navy);background:#fff;overflow:hidden;box-shadow:0 6px 8px -4px rgba(0,0,0,.25)}
.hero h1{position:absolute;left:21px;top:25px;font-size:15px;font-weight:400;color:var(--blue)}
.hero p{position:absolute;left:21px;top:50px;width:330px;font-size:8.4px;line-height:16px;color:#333}
.hero-photo{position:absolute;left:350px;top:0;width:340px;height:143px;background:linear-gradient(90deg,#fff 0,#c8d6e4 22%,#3b5677 55%,#8fa6bf 80%,#dfe6ee)}
.dots{position:absolute;left:14px;top:124px;display:flex;gap:9px}
.dots i{width:6px;height:6px;border-radius:50%;background:#222}
.dots i:first-child{background:var(--blue)}
.nav{left:0;top:242px;width:811px;height:39px;background:linear-gradient(#2d78c0,#1a5696);border-bottom:1px solid #12406f}
.nav ul{position:absolute;left:61px;top:0;display:flex;list-style:none;height:39px}
.nav li{height:39px;border-left:1px solid #164a83;border-right:1px solid #3a86cc;color:#fff;font-size:10px;display:flex;align-items:center;justify-content:center}
.nav li.active{background:linear-gradient(#5b9fdb,#3c84c8)}
.flags{gap:6px}
.section-tab{left:61px;top:306px;width:102px;height:23px;background:#3a3a3a;color:#fff;font-size:11.5px;display:flex;align-items:center;justify-content:center}
.section-rule{left:168px;top:318px;width:584px;height:1px;background:#8a8a8a}
.listing{position:absolute;width:162px;height:154px;background:var(--card);border:1px solid #e2e2e2;box-shadow:0 2px 2px rgba(0,0,0,.12)}
.listing-logo{position:absolute;left:4px;top:4px;width:153px;height:64px;display:flex;align-items:center;justify-content:center;gap:7px;font-size:13px;font-weight:700;border:1px solid #ddd;background:#fff;color:var(--navy)}
.listing-logo .mark{width:10px;height:10px;background:var(--mark)}
.listing h3{position:absolute;left:16px;top:75px;font-size:10px;font-weight:400;color:var(--link)}
.listing p{position:absolute;left:16px;top:92px;width:140px;font-size:8.2px;line-height:12px;color:#8a8a8a}
.actions{position:absolute;left:16px;top:126px;display:flex;align-items:center}
.view-btn{width:54px;height:15px;background:var(--btn);color:#fff;font-size:8px;display:flex;align-items:center;justify-content:center;margin-right:17px}
.ico{width:17px;height:15px;background:var(--btn);display:flex;align-items:center;justify-content:center;margin-right:5px}
.promo{background:#1a1a1a;border-color:#1a1a1a;flex-direction:column;align-items:flex-start;justify-content:flex-start;padding:10px 8px;color:#f2b400;font-size:9.5px;font-weight:400}
.promo .stars{color:#f2b400;font-size:9px;margin-top:8px;letter-spacing:1px}
.promo .apply{position:absolute;right:12px;top:34px;background:#2e6fbd;color:#fff;font-size:7.5px;padding:3px 9px;border-radius:3px}
.card-photo{width:60px;height:38px;border-radius:3px;background:linear-gradient(135deg,#666,#2a2a2a)}
.rule{left:61px;width:691px;height:1px;background:var(--rule)}
.category{position:absolute;top:873px;width:162px;height:27px;background:linear-gradient(#3a7cc0,#24609f);color:#fff;font-size:10px;display:flex;align-items:center;justify-content:center;gap:6px}
.category::before{content:"";border-left:4px solid #fff;border-top:3.5px solid transparent;border-bottom:3.5px solid transparent}
.feature h2{position:absolute;top:932px;font-size:13px;font-weight:400;color:var(--navy)}
.more-arrow{position:absolute;top:933px;width:12px;height:12px;border-radius:50%;background:#666}
.more-arrow::after{content:"";position:absolute;left:4.5px;top:3px;border-left:4px solid #fff;border-top:3px solid transparent;border-bottom:3px solid transparent}
.feature-box{position:absolute;top:956px;width:217px;height:172px;background:#fff;border:1px solid #ececec;box-shadow:0 0 4px rgba(0,0,0,.12)}
.feature-photo{position:absolute;left:18px;top:17px;width:181px;height:77px;border:2px solid #eee}
.feature-box h4{position:absolute;left:18px;top:103px;font-size:9.5px;font-weight:400;color:var(--link)}
.feature-box p{position:absolute;left:18px;top:119px;width:181px;font-size:8.2px;line-height:13px;color:#777;text-align:justify}
.feature-box em{position:absolute;left:18px;top:147px;font-size:7.5px;color:#777}
.video-frame{position:absolute;left:11px;top:9px;width:200px;height:153px;background:linear-gradient(120deg,#6e87a6,#b7c6d6 45%,#4f6581)}
.play{position:absolute;left:74px;top:60px;width:50px;height:32px;background:#111;border-radius:5px}
.play::after{content:"";position:absolute;left:19px;top:8px;border-left:15px solid #fff;border-top:8px solid transparent;border-bottom:8px solid transparent}
.footer-links{left:61px;top:1164px;font-size:8.5px;color:#777;word-spacing:1px}
.footer-links span{margin:0 5px;color:#aaa}
.copyright{left:61px;top:1185px;font-size:8.5px;color:#777}
.social{left:661px;top:1170px;display:flex;gap:6px}
.social i{width:18px;height:18px;border-radius:50%;background:#666;display:flex;align-items:center;justify-content:center}
</style>
</head>
<body>
<svg width="0" height="0" style="position:absolute">
  <symbol id="i-search" viewBox="0 0 12 12"><circle cx="5" cy="5" r="3.3" fill="none" stroke="#fff" stroke-width="1.6"/><path d="M7.4 7.4 10.5 10.5" stroke="#fff" stroke-width="1.8"/></symbol>
  <symbol id="i-heart" viewBox="0 0 12 12"><path d="M6 10.5 1.5 6A2.4 2.4 0 0 1 6 2.8 2.4 2.4 0 0 1 10.5 6Z" fill="#fff"/></symbol>
  <symbol id="i-star" viewBox="0 0 12 12"><path d="M6 .8 7.5 4.2 11.2 4.5 8.4 7 9.2 10.7 6 8.8 2.8 10.7 3.6 7 .8 4.5 4.5 4.2Z" fill="#fff"/></symbol>
</svg>

<div class="abs header-bg"></div>
<div class="abs brand">VESTRANO</div>
<div class="abs search">Search
  <svg width="8" height="8" viewBox="0 0 12 12"><circle cx="5" cy="5" r="3.3" fill="none" stroke="#aaa" stroke-width="1.5"/><path d="M7.4 7.4 10.5 10.5" stroke="#aaa" stroke-width="1.6"/></svg>
</div>

<section class="abs hero">
  <div class="hero-photo" role="img" aria-label="Business people reviewing documents at a desk"></div>
  <h1>Welcome to our site</h1>
  <p>Pellentesque eget lacus nunc, eu lobortis felis. Suspendisse potenti. Praesent sapien sapien, condimentum eget pretium ac, vulputate eget mauris. Lorem ipsum dolor sit amet, consectetur adipiscing elit. Fusce sit amet egestas ligula.</p>
  <div class="dots"><i></i><i></i><i></i><i></i></div>
</section>

<nav class="abs nav">
  <ul>
    <li class="active" style="width:69px">HOME</li>
    <li style="width:90px">ABOUT US</li>
    <li style="width:140px">FINANCE DICTIONARY</li>
    <li style="width:114px">ABOUT FINANCE</li>
    <li style="width:76px">FORUM</li>
    <li style="width:99px">CONTACT US</li>
    <li class="flags" style="width:101px">
      <svg width="15" height="11" viewBox="0 0 3 2"><rect width="1" height="2" fill="#1f3f99"/><rect x="1" width="1" height="2" fill="#fff"/><rect x="2" width="1" height="2" fill="#d62828"/></svg>
      <svg width="15" height="11" viewBox="0 0 3 4"><rect width="3" height="4" fill="#c8102e"/><rect y="1" width="3" height="2" fill="#f5c400"/></svg>
      <svg width="15" height="11" viewBox="0 0 30 20"><rect width="30" height="20" fill="#1f3f99"/><path d="M0 0 30 20M30 0 0 20" stroke="#fff" stroke-width="4"/><path d="M15 0v20M0 10h30" stroke="#fff" stroke-width="6"/><path d="M15 0v20M0 10h30" stroke="#c8102e" stroke-width="3"/></svg>
    </li>
  </ul>
</nav>

<div class="abs section-tab">Latest Listing</div>
<div class="abs section-rule"></div>

<!-- Row 1 -->
<article class="listing" style="left:61px;top:349px">
  <div class="listing-logo">Kvikla</div>
  <h3>Kvikla</h3>
  <p>FORBRUKSLÅN. Petter fra Kvikla hjelper deg med små og store lån...</p>
  <div class="actions"><span class="view-btn">View more</span><span class="ico"><svg width="10" height="10"><use href="#i-search"/></svg></span><span class="ico"><svg width="10" height="10"><use href="#i-heart"/></svg></span><span class="ico"><svg width="10" height="10"><use href="#i-star"/></svg></span></div>
</article>
<article class="listing" style="left:237px;top:349px">
  <div class="listing-logo">Aldermoor Bank</div>
  <h3>Kvikla</h3>
  <p>FORBRUKSLÅN. Petter fra Kvikla hjelper deg med små og store lån...</p>
  <div class="actions"><span class="view-btn">View more</span><span class="ico"><svg width="10" height="10"><use href="#i-search"/></svg></span><span class="ico"><svg width="10" height="10"><use href="#i-heart"/></svg></span><span class="ico"><svg width="10" height="10"><use href="#i-star"/></svg></span></div>
</article>
<article class="listing" style="left:413px;top:349px">
  <div class="listing-logo">fjordvik.example</div>
  <h3>Kvikla</h3>
  <p>FORBRUKSLÅN. Petter fra Kvikla hjelper deg med små og store lån...</p>
  <div class="actions"><span class="view-btn">View more</span><span class="ico"><svg width="10" height="10"><use href="#i-search"/></svg></span><span class="ico"><svg width="10" height="10"><use href="#i-heart"/></svg></span><span class="ico"><svg width="10" height="10"><use href="#i-star"/></svg></span></div>
</article>
<article class="listing" style="left:589px;top:349px">
  <div class="listing-logo">Solterra Bank</div>
  <h3>Kvikla</h3>
  <p>FORBRUKSLÅN. Petter fra Kvikla hjelper deg med små og store lån...</p>
  <div class="actions"><span class="view-btn">View more</span><span class="ico"><svg width="10" height="10"><use href="#i-search"/></svg></span><span class="ico"><svg width="10" height="10"><use href="#i-heart"/></svg></span><span class="ico"><svg width="10" height="10"><use href="#i-star"/></svg></span></div>
</article>

<!-- Row 2 -->
<article class="listing" style="left:61px;top:518px">
  <div class="listing-logo">Tallfinans</div>
  <h3>Kvikla</h3>
  <p>FORBRUKSLÅN. Petter fra Kvikla hjelper deg med små og store lån...</p>
  <div class="actions"><span class="view-btn">View more</span><span class="ico"><svg width="10" height="10"><use href="#i-search"/></svg></span><span class="ico"><svg width="10" height="10"><use href="#i-heart"/></svg></span><span class="ico"><svg width="10" height="10"><use href="#i-star"/></svg></span></div>
</article>
<article class="listing" style="left:237px;top:518px">
  <div class="listing-logo">Meridum</div>
  <h3>Kvikla</h3>
  <p>FORBRUKSLÅN. Petter fra Kvikla hjelper deg med små og store lån...</p>
  <div class="actions"><span class="view-btn">View more</span><span class="ico"><svg width="10" height="10"><use href="#i-search"/></svg></span><span class="ico"><svg width="10" height="10"><use href="#i-heart"/></svg></span><span class="ico"><svg width="10" height="10"><use href="#i-star"/></svg></span></div>
</article>
<article class="listing" style="left:413px;top:518px">
  <div class="listing-logo promo">10.000 - 350.000 - 1-14 Year<span class="stars">★★★★☆</span><span class="apply">Apply Now</span></div>
  <h3>Fjordvik Card</h3>
  <p>FORBRUKSLÅN. Petter fra Kvikla hjelper deg med små og store lån...</p>
  <div class="actions"><span class="view-btn">View more</span><span class="ico"><svg width="10" height="10"><use href="#i-search"/></svg></span><span class="ico"><svg width="10" height="10"><use href="#i-heart"/></svg></span><span class="ico"><svg width="10" height="10"><use href="#i-star"/></svg></span></div>
</article>
<article class="listing" style="left:589px;top:518px">
  <div class="listing-logo"><span class="card-photo" role="img" aria-label="Photo of a payment card"></span></div>
  <h3>Kvikla</h3>
  <p>FORBRUKSLÅN. Petter fra Kvikla hjelper deg med små og store lån...</p>
  <div class="actions"><span class="view-btn">View more</span><span class="ico"><svg width="10" height="10"><use href="#i-search"/></svg></span><span class="ico"><svg width="10" height="10"><use href="#i-heart"/></svg></span><span class="ico"><svg width="10" height="10"><use href="#i-star"/></svg></span></div>
</article>

<!-- Row 3 -->
<article class="listing" style="left:61px;top:689px">
  <div class="listing-logo">Lanvo</div>
  <h3>Kvikla</h3>
  <p>FORBRUKSLÅN. Petter fra Kvikla hjelper deg med små og store lån...</p>
  <div class="actions"><span class="view-btn">View more</span><span class="ico"><svg width="10" height="10"><use href="#i-search"/></svg></span><span class="ico"><svg width="10" height="10"><use href="#i-heart"/></svg></span><span class="ico"><svg width="10" height="10"><use href="#i-star"/></svg></span></div>
</article>
<article class="listing" style="left:237px;top:689px">
  <div class="listing-logo">Bryggelånet</div>
  <h3>Kvikla</h3>
  <p>FORBRUKSLÅN. Petter fra Kvikla hjelper deg med små og store lån...</p>
  <div class="actions"><span class="view-btn">View more</span><span class="ico"><svg width="10" height="10"><use href="#i-search"/></svg></span><span class="ico"><svg width="10" height="10"><use href="#i-heart"/></svg></span><span class="ico"><svg width="10" height="10"><use href="#i-star"/></svg></span></div>
</article>
<article class="listing" style="left:413px;top:689px">
  <div class="listing-logo"><i class="mark"></i>Orvento</div>
  <h3>Kvikla</h3>
  <p>FORBRUKSLÅN. Petter fra Kvikla hjelper deg med små og store lån...</p>
  <div class="actions"><span class="view-btn">View more</span><span class="ico"><svg width="10" height="10"><use href="#i-search"/></svg></span><span class="ico"><svg width="10" height="10"><use href="#i-heart"/></svg></span><span class="ico"><svg width="10" height="10"><use href="#i-star"/></svg></span></div>
</article>
<article class="listing" style="left:589px;top:689px">
  <div class="listing-logo">Marvika Bank</div>
  <h3>Kvikla</h3>
  <p>FORBRUKSLÅN. Petter fra Kvikla hjelper deg med små og store lån...</p>
  <div class="actions"><span class="view-btn">View more</span><span class="ico"><svg width="10" height="10"><use href="#i-search"/></svg></span><span class="ico"><svg width="10" height="10"><use href="#i-heart"/></svg></span><span class="ico"><svg width="10" height="10"><use href="#i-star"/></svg></span></div>
</article>

<div class="abs rule" style="top:858px"></div>
<a class="category" style="left:61px">CONSUMER LENDING</a>
<a class="category" style="left:237px">CAR LOANS</a>
<a class="category" style="left:413px">UNSECURED LOANS</a>
<a class="category" style="left:590px">CONSUMER LOANS</a>
<div class="abs rule" style="top:917px"></div>

<section class="feature">
  <h2 style="left:61px">About Personal Loans</h2>
  <span class="more-arrow" style="left:266px"></span>
  <div class="feature-box" style="left:61px">
    <div class="feature-photo" role="img" aria-label="Woman working on a laptop" style="background:linear-gradient(90deg,#c9c2b4,#9a8f7f 40%,#dfe2df)"></div>
    <h4>Sed vestibulum tellus</h4>
    <p>Enim eleifend feugiat. Duis id ante ac metus auctor porttitor.</p>
    <em>View more</em>
  </div>
</section>
<section class="feature">
  <h2 style="left:297px">Latest Article</h2>
  <span class="more-arrow" style="left:503px"></span>
  <div class="feature-box" style="left:297px">
    <div class="feature-photo" role="img" aria-label="Man writing at an office desk" style="background:linear-gradient(90deg,#f1f1f1,#d9d4cc 50%,#8a6a55 75%,#e9e9e9)"></div>
    <h4>Sed vestibulum tellus</h4>
    <p>Enim eleifend feugiat. Duis id ante ac metus auctor porttitor.</p>
    <em>View more</em>
  </div>
</section>
<section class="feature">
  <h2 style="left:533px">How it works Video</h2>
  <div class="feature-box" style="left:534px">
    <div class="video-frame" role="img" aria-label="Video still of a loan advisor meeting a client"><span class="play"></span></div>
  </div>
</section>

<div class="abs rule" style="top:1148px"></div>
<div class="abs footer-links">Home<span>|</span>About Us<span>|</span>Finance Dictionary<span>|</span>About Finance<span>|</span>Forum<span>|</span>Contact Us</div>
<div class="abs copyright">Copyright © 2012 &nbsp; www.vestrano.example &nbsp; All rights reserved.</div>
<div class="abs social">
  <i></i><i></i><i></i>
  <i><svg width="10" height="8" viewBox="0 0 10 8"><rect x=".5" y=".5" width="9" height="7" fill="none" stroke="#fff"/><path d="M.5.5 5 4.5 9.5.5" fill="none" stroke="#fff"/></svg></i>
</div>
</body>
</html>
```